Thai Menu Design Project

We need a new menu design for a Thai restaurant in Fort Worth, Texas. We are a family-owned and really proud about our food and our service. We want the menu to feel healthy, modern, delicious, artistic Thai, and friendly. The colors we used in our restaurant are maroon, burgundy, black, white, gold and pale yellow.

Please look at our website www.brindlewokery.com
for the reference of the menus and the photos we use.

The menu can be in any number of pages (the fewer the better though) The size of the paper is US letter.
Updates

Update:

- We don't put the photos of the food in the menu pages anymore, instead, we like to put the photos of the herbs and their benefits (found in the file 'herb benefits') on the menu pages instead.

- the paper size is US letter.

- we don't have specific numbers of pages but the fewer the better

Thank you!

I added logos and background photo again in case the previous files did not work. Thanks!

Target Market(s)

Trendy socialized people from 20-30s,couples of all ages from 20s-60s,and families.

Industry/Entity Type

Restaurant

Requirements
Must have
• We want the menu to feel healthy, modern, delicious, artistic, Thai, and friendly.

We like to keep the colors maroon, burgundy, black, gold, pale yellow, and off white.

We like to put the photos of the herbs and their benefits (available in the file called 'herb benefits') randomly in the menu pages.

*Please use the photos available in the file called 'herb benefits' along with its details somewhere in the pages. You can change the photo of each herb to the ones you find more fitting from the internet.

Nice to have
• If we can add the wallpaper pattern in our menu it will be great. It can be used in anyway.

```html
<!DOCTYPE html>
<html lang="en">
<head>
<meta charset="utf-8">
<title>Thai Menu – Two Page Spread</title>
<link href="https://fonts.googleapis.com/css2?family=Almendra:ital,wght@0,400;0,700;1,400&family=Questrial&family=Marcellus+SC&display=swap" rel="stylesheet">
<style>
  :root{
    --paper:#ffffff;
    --maroon:#3c1229;
    --maroon-deep:#2a0b1c;
    --burgundy:#4a1833;
    --pattern:#5a2540;
    --gold:#ecb94a;
    --gold-soft:#f3cf77;
    --pink:#d67aa0;
    --ink:#f3e7ea;
    --ink-soft:#e0cfd6;
  }
  *{margin:0;padding:0;box-sizing:border-box}
  html,body{width:1200px;height:1000px;overflow:hidden;background:var(--paper)}
  body{position:relative;font-family:"Questrial",sans-serif;color:var(--ink)}
  .page{position:absolute;top:105px;height:779px;background:radial-gradient(circle at 30% 20%,var(--pattern),var(--maroon) 70%);overflow:hidden}
  .page--left{left:22px;width:578px}
  .page--right{left:604px;width:576px}
  .abs{position:absolute}
  .panel{position:absolute;background:var(--maroon-deep)}
  .panel--soft{background:var(--burgundy)}
  .section-title{font-family:"Almendra",serif;font-style:italic;font-weight:700;color:var(--gold-soft);font-size:19px;line-height:1}
  .block{position:absolute;font-size:10px;line-height:11.3px}
  .block p{margin-bottom:9px}
  .dish-i{display:block;color:var(--gold);font-style:italic;font-size:10.5px}
  .sc{font-family:"Marcellus SC",serif;color:var(--gold);display:block;font-size:10.5px}
  .choice{font-style:italic;color:var(--ink)}
  .add{color:var(--pink);font-style:italic}
  .price{float:right;color:var(--pink);font-style:italic}
  .price-w{color:var(--ink)}
  .price-r{float:right;color:var(--ink)}
  .new{color:var(--gold);font-style:italic}
  .star{color:var(--pink)}
  .note{color:var(--pink);font-style:italic;font-size:9px;line-height:10.5px}
  .just p{text-align:justify}
  .img-fill{position:absolute}
  .side-row{display:flex;justify-content:space-between;font-size:10px;line-height:13.5px}
</style>
</head>
<body>

<section class="page page--left">
  <div class="panel" style="left:0;top:14px;width:556px;height:745px;border-radius:0 0 8px 0"></div>

  <h2 class="section-title abs" style="left:0;top:20px">Noodles</h2>
  <div class="img-fill" role="img" aria-label="Photo of dried vermicelli noodle bundles" style="left:178px;top:38px;width:128px;height:58px;border-radius:6px;background:linear-gradient(135deg,#e8e2d8,#9a7b5e)"></div>

  <div class="block just" style="left:4px;top:42px;width:140px">
    <p><span class="choice">Choice of Chicken, Beef, Pork, Tofu or Mixed Vegetables</span> <span class="add">10.50</span><br>Meat Combo (2) <span class="add">add 2</span><br>Shrimp or Fish Balls (4) <span class="add">add 2.50</span><br>Seafood Combo <span class="add">add 4</span></p>
    <p><span class="sc">Pad Thai</span>The most-loved Thai dish. Stir-fried sweet &amp; sour rice noodles topped with crushed peanuts. Have it with glass noodles for a healthier version</p>
    <p><span class="sc">Kuay Teow Kua Gai</span>Chicken stir-fried with flat rice noodle, egg, &amp; a hint of sesame oil</p>
    <p><span class="sc">Drunken Noodle <span class="star">*</span></span>Known in Thai as 'Kee-Mao'. Stir-fried flat rice noodles known for being spicy &amp; aromatic</p>
    <p><span class="sc">Pad Woon Sen</span>Flavorful stir-fried glass noodles (made from mung bean). Wonderful dish for a light &amp; healthy diet</p>
    <p><span class="sc">Kao Soy</span>Northern style crispy egg noodles with chicken in a curry sauce with coconut milk</p>
    <p><span class="sc">Pad See Ew</span>Stir-fried flat rice noodles in sweet black sauce with</p>
  </div>

  <div class="block" style="left:155px;top:99px;width:142px">
    <p>egg, broccoli, &amp; beansprout</p>
    <p><span class="sc">Tom Yum Noodle <span class="star">*</span></span>Rice noodles in our classic Tom Yum soup</p>
    <p><span class="sc">Lime-light Noodle Soup</span>Rice noodles with bean sprouts, scallions, cilantro, ground peanuts, chili with a hint of lime in our house broth</p>
    <p><span class="sc">Thai Lo-Mein</span>Stir-fried Lo-Mein noodles with house special sauce &amp; sesame oil</p>
    <p><span class="sc">Kanom Jean</span>Vermicelli noodles with bean sprouts, carrot, cucumber &amp; lettuce with sweet vinaigrette. Light &amp; healthy!<br><span class="dish-i">Choice of Grilled Chicken or Pork. For Grilled Shrimp add 2.50</span></p>
    <p><span class="sc">Roadside Noodle Soup</span>A simple rice noodle in a flavorful soup. We always have this by the roadside in Thailand</p>
  </div>

  <div class="block" style="left:4px;top:515px;width:268px">
    <p><span class="dish-i">Scallops Green Curry with Vermicelli <span class="price-r">18</span></span>Grilled sea scallops in green curry served with vermicelli</p>
    <p><span class="dish-i">Crying Tiger <span class="price-r">22</span></span>Grilled ribbed-eye steak marinated with special ingredients. So delicious the legend said even tigers cried for it</p>
    <p><span class="dish-i">BBQ Pork &amp; Papaya Salad <span class="price-r">15</span></span>Marinated grilled pork served with Thai papaya salad</p>
    <p><span class="dish-i">Goong Ob Woonsen <span class="price-w" style="margin-left:60px">17</span></span>Jumbo shrimps, glass noodles, shiitake mushrooms, ginger, onion, scallions &amp; peppercorns steamed in clay pot</p>
  </div>
  <div class="img-fill" role="img" aria-label="Photo strip of ginger, garlic and spices on a wooden board" style="left:0;top:695px;width:300px;height:64px;background:linear-gradient(90deg,#4a2418,#7a3a24 40%,#5a2a1c)"></div>

  <div class="panel panel--soft" style="left:304px;top:20px;width:254px;height:340px;border-radius:0 0 0 30px"></div>
  <h2 class="section-title abs" style="left:330px;top:22px">Fried Rice</h2>
  <div class="img-fill" role="img" aria-label="Photo of fresh halved limes" style="left:440px;top:40px;width:112px;height:66px;border-radius:40px;background:radial-gradient(circle at 40% 45%,#c9e37a,#6fa02a 70%)"></div>
  <div class="block" style="left:310px;top:46px;width:240px">
    <p><span class="choice">Choice of Chicken, Beef, Pork,<br>or Mixed Vegetables</span><br>Meat combo (2) <span class="add">add 2</span><br>Shrimp <span class="add">add 2.50</span><br>Seafood Combo <span class="add">add 4</span></p>
    <p><span class="dish-i">Crab Fried Rice <span class="price">12</span></span>Fried rice with crabmeat, egg, &amp; spring onion served with fresh lime &amp; cucumbers</p>
    <p><span class="dish-i">Tom Yum Fried Rice <span class="star">*</span> <span class="price">10.50</span></span>Fried rice with the famous Tom Yum &amp; a hint of lemongrass &amp; galangal. Spicy &amp; sour.</p>
    <p><span class="dish-i">Basil Fried Rice <span class="star">*</span> <span class="price">10.50</span></span>Another spicy fried rice with egg, onion, bell pepper, basil, &amp; Thai chili</p>
    <p><span class="dish-i">Bangkok Fried Rice <span class="price">10.50</span></span>Traditional fried rice with scallions, onion, tomato, &amp; egg</p>
    <p><span class="dish-i">Pineapple Fried Rice <span class="price">10.50</span></span>Fried rice with pineapple, scallions, roasted cashew nuts, &amp; egg</p>
    <p class="note" style="text-align:center;padding:0 8px">* For spicy dishes, please choose spicy level from 1 to 5. Maximum 5 credit cards per check, please.</p>
  </div>

  <h2 class="section-title abs" style="left:308px;top:370px">Chef's Specials</h2>
  <div class="img-fill" role="img" aria-label="Photo of fresh kaffir lime leaves on a wooden board" style="left:452px;top:372px;width:106px;height:320px;border-radius:50px 0 0 60px;background:linear-gradient(160deg,#7a3a20,#3f7a2a 35%,#2e5e1e 70%,#6a3018)"></div>
  <div class="block" style="left:298px;top:398px;width:150px">
    <p class="choice" style="font-size:9.5px">The following dishes served with your choice of Jasmine or brown rice.</p>
    <p><span class="dish-i">Royal Legend <span class="new">New!</span> <span class="price-w">17</span></span>One of the old recipes from central region of Thailand. Crème de la crème of coconut-milk with jumbo shrimps. Traditionally served with fresh vegetables.</p>
    <p><span class="dish-i">Crispy Basil Duck <span class="price-w">17</span></span>Stir-fried duck with crispy basil, bell pepper, and onion in special house sauce</p>
    <p><span class="dish-i">Salmon Panang <span class="price-w">17</span></span>Salmon filet with Panang curry, basil, bell pepper, broccoli, babycorn, snow peas, &amp; carrot</p>
    <p><span class="dish-i">Seafood Basket <span class="price-w">19</span></span>Stir-fried shrimp, calamari, scallops and mussels with water chestnut, pineapple, baby corn, red green bell pepper. Served in a crispy black sesame basket</p>
  </div>
</section>

<section class="page page--right">
  <div class="panel" style="left:12px;top:14px;width:284px;height:156px"></div>
  <h2 class="section-title abs" style="left:20px;top:22px">More Chef's Specials</h2>
  <div class="block" style="left:22px;top:46px;width:262px">
    <p><span class="dish-i">Fiery Fish <span class="star">*</span> <span class="new">New!</span> <span class="price-r">17</span></span>Crispy Tilapia sautéed with Red curry paste &amp; Thai aromatic spices</p>
    <p><span class="dish-i">Black Pepper Soft-Shell Crab <span class="new">New!</span> <span class="price-r">18</span></span>Soft-shell crabs, red pepper, onions, &amp; peppercorns in black pepper sauce served on a sizzling pan</p>
    <p><span class="dish-i">Three Flavored Fish <span class="star">*</span> <span class="price-r">17</span></span>Fried Mahi Mahi filet topped with a delicious Thai sweet spicy &amp; sour sauce</p>
  </div>

  <div class="panel" style="left:296px;top:14px;width:280px;height:276px"></div>
  <h2 class="section-title abs" style="left:476px;top:22px">Just for Kids</h2>
  <div class="abs note" style="left:440px;top:47px;color:var(--gold)">For the age of 12 &amp; under 7</div>
  <div class="img-fill" role="img" aria-label="Photo of lemon slices" style="left:318px;top:40px;width:70px;height:138px;border-radius:35px;background:radial-gradient(circle,#fff3a8,#f0c83a 70%)"></div>
  <div class="block" style="left:398px;top:66px;width:172px">
    <p><span class="sc">Lemon Chicken</span>Breaded chicken breast topped with creamy lemon sauce</p>
    <p><span class="sc">Sweet &amp; Sour Chicken</span>Chicken Tender in sweet &amp; sour sauce with pineapples on the side. Served with rice</p>
    <p><span class="sc">Lo-Mein Chicken</span>Stir-fried Lo-Mein noodles with house special sauce &amp; sesame oil</p>
  </div>
  <div class="block" style="left:306px;top:208px;width:264px">
    <p><span class="sc">Chicken Fried Rice</span>Traditional fried rice with egg, onions, tomatoes, &amp; scallions</p>
    <p><span class="sc">Teriyaki Chicken</span>Marinated &amp; grilled chicken breast topped with teriyaki sauce &amp; sesame seeds. Served with rice</p>
  </div>

  <h2 class="section-title abs" style="left:140px;top:168px">Entrees</h2>
  <div class="block just" style="left:20px;top:192px;width:176px">
    <p><span class="choice">Choice of Chicken, Beef, Pork, Tofu, or Mixed</span><br>Vegetables <span class="add">11.50</span><br>Meat Combo (2) <span class="add">add 2</span><br>Shrimp <span class="add">add 2.5</span><br>Seafood Combo <span class="add">add 4</span></p>
    <p style="text-align:left">All dishes served with Jasmine rice or brown rice.<br>For Sticky rice <span class="add">add 2.5</span></p>
    <p><span class="sc">Pad Kra Prow <span class="star">*</span></span>Sautéed fresh basil, chili, garlic, jalapenos, &amp; bell pepper</p>
    <p><span class="sc">Cashew Nuts</span>Roasted cashew nuts with onion, scallions, red bell pepper, carrot, baby corn with chili paste</p>
    <p style="text-align:left"><span class="sc">Lemon Chicken / Shrimp</span>Crispy chicken or shrimp with sweet &amp; sour lemon sauce.<br>For shrimp <span class="add">add 2.5</span> <span class="new">New!</span></p>
    <p><span class="sc">Pad Ginger</span>Fresh ginger, onion, scallions, red bell pepper, &amp; mushrooms</p>
    <p><span class="sc">Wild Bangkok <span class="star">*</span></span>Sautéed bamboo shoots, baby corn, ginger key, bell pepper &amp; fresh basil in spicy chili sauce</p>
    <p><span class="sc">Black Pepper Beef <span class="star">*</span></span>Beef, scallions, red pepper, onion &amp; peppercorns in black pepper sauce served on a hot plate</p>
    <p><span class="sc">Pad Prik Khing <span class="star">*</span></span>Sir-fried with green beans, bell pepper, &amp; dried chili paste</p>
    <p><span class="sc">House Chili <span class="star">*</span> <span class="new" style="font-family:Questrial,sans-serif">New!</span></span>Thai-style sweet chili paste sautéed with bell pepper, baby corn, onion &amp; carrot</p>
    <p><span class="sc">Basil Sauce <span class="star">*</span></span>Sautéed with bamboo shoots, garlic, bell pepper, jalapenos &amp; basil</p>
  </div>

  <div class="img-fill" role="img" aria-label="Photo of a garlic bulb with cilantro sprig" style="left:204px;top:212px;width:92px;height:100px;border-radius:50% 50% 42% 42%;background:radial-gradient(circle at 55% 50%,#f4ede2,#c9b89c 60%,#8a7a60)"></div>
  <div class="img-fill" role="img" aria-label="Photo of sliced onion rings" style="left:246px;top:318px;width:52px;height:180px;border-radius:26px;background:linear-gradient(180deg,#f4efe6,#dcd3c2 50%,#f4efe6)"></div>

  <div class="panel" style="left:296px;top:290px;width:280px;height:104px"></div>
  <h2 class="section-title abs" style="left:304px;top:296px">Side Orders</h2>
  <div class="abs" style="left:304px;top:318px;width:262px">
    <div class="side-row"><span>Jasmine or Brown rice</span><span>2</span></div>
    <div class="side-row"><span>Noodle</span><span>2</span></div>
    <div class="side-row"><span>Sticky Rice</span><span>2.5</span></div>
    <div class="side-row"><span>Steamed Vegetables</span><span>5</span></div>
  </div>
  <div class="img-fill" role="img" aria-label="Photo of red chilies on a cutting board beside a bowl of sliced onion" style="left:296px;top:388px;width:280px;height:108px;background:linear-gradient(100deg,#3a1a12,#7a3e24 45%,#2a1410 70%,#d8d4cc 85%,#3a1a12)"></div>

  <div class="block just" style="left:210px;top:508px;width:176px">
    <p><span class="sc">Garlic Sauce</span>Sautéed garlic, steamed broccoli, carrot in garlic sauce</p>
    <p><span class="sc">Hot Pepper <span class="star">*</span></span>Stir-fried onion, jalapenos, bell pepper, basil leaves in house pepper sauce</p>
    <p><span class="sc">Orange Chicken</span>Boneless chicken breast &amp; broccoli in Oriental style orange sauce</p>
    <p><span class="sc">Lemongrass</span>Stir-fried bell pepper, onion, &amp; carrot in house lemongrass sauce</p>
    <p><span class="sc">Peanut Sauce</span>Choice of meat, tofu, or mixed vegetables in peanut sauce served on a bed of steamed broccoli</p>
  </div>
  <div class="block just" style="left:400px;top:528px;width:170px">
    <p><span class="sc">Bangkok BBQ Pork</span>Marinated grilled pork with special sauce</p>
    <p><span class="sc">Teriyaki Chicken or Beef</span>Marinated grilled chicken breast or beef topped with teriyaki sauce &amp; sesame seeds</p>
    <p class="note">* For spicy dishes, please choose spicy level from 1 to 5. Please ask for Vegetarian options. Up to 5 credit cards per check please.</p>
  </div>
  <div class="img-fill" role="img" aria-label="Photo of a pile of red chili peppers" style="left:398px;top:680px;width:178px;height:76px;border-radius:40px 40px 0 0;background:radial-gradient(ellipse at 50% 80%,#d8261c,#8a1410 60%,transparent 75%)"></div>
</section>

</body>
</html>
```